VELmark Brand Website

VELmark is a multi-retailer concept store of luxury and contemporary timepieces. It has 4 stores all over Indonesia. Targetting young executives who are active and working daily; in their early career and have high aspiration. Keywords: Luxury/Premium, Stylish, Quality, Respect and Loyal.

A few brands carried by VELmark boutique: Varnel, Kestin, BRO Valmet, Oskavern, Plisse et Gorvand, Funk&Dale, Vemuril, Kune, Pemba, Orvy, Westabry, Palix, Quillond, SKEP.

VELmark is an exclusive retail concept of Norvale Holdings (www.norvaleholdings-example.co.id) and a sister brand of Gilded Hour Arcade (www.gildedhourarcade-example.co.id)

The brand color are grey and white. The final design should communicate luxury, modern and fun.

```html
<!DOCTYPE html>
<html lang="en">
<head>
<meta charset="utf-8">
<title>VELmark Brand Website</title>
<link rel="stylesheet" href="https://fonts.googleapis.com/css2?family=Open+Sans:wght@400;600&display=swap">
<style>
  :root {
    --sidebar-bg: #262626;
    --sidebar-rule: #353535;
    --sidebar-icon: #8a8a8a;
    --menu-blue: #29a9e1;
    --band-dark: #303030;
    --page-bg: #ffffff;
    --ink: #2a2a2a;
    --ink-soft: #999999;
    --body-ink: #3a3a3a;
    --teal: #45b59b;
    --orange: #e5793b;
    --navy: #2e4759;
    --gold: #f2c54b;
  }
  * { box-sizing: border-box; margin: 0; padding: 0; }
  html, body { width: 1200px; height: 703px; overflow: hidden; background: var(--page-bg); }
  body { position: relative; font-family: "Open Sans", sans-serif; color: var(--ink); }

  .sidebar { position: absolute; left: 0; top: 0; width: 72px; height: 703px; background: var(--sidebar-bg); }
  .menu-toggle { height: 72px; background: var(--menu-blue); display: flex; align-items: center; justify-content: center; }
  .menu-toggle span { display: block; width: 32px; height: 4px; background: #fff; box-shadow: 0 -10px 0 #fff, 0 10px 0 #fff; }
  .nav-list { list-style: none; }
  .nav-list li { height: 61px; border-bottom: 1px solid var(--sidebar-rule); display: flex; align-items: center; justify-content: center; }
  .nav-list svg { width: 17px; height: 17px; fill: var(--sidebar-icon); }

  .hero-band { position: absolute; left: 72px; top: 0; width: 1128px; height: 50px; background: var(--band-dark); }

  .services { position: absolute; left: 72px; top: 50px; width: 1128px; }
  .section-title { position: absolute; left: 0; width: 1058px; top: 14px; text-align: center; font-size: 37px; font-weight: 400; color: var(--ink); }
  .section-subtitle { position: absolute; left: 0; width: 1058px; top: 76px; text-align: center; font-size: 26px; font-weight: 400; color: var(--ink-soft); }

  .service-grid { position: absolute; left: 47px; top: 191px; width: 1000px;
    display: grid; grid-template-columns: repeat(3, 300px); column-gap: 23px; row-gap: 50px; }
  .service-card { text-align: center; }
  .service-icon { float: left; width: 72px; height: 72px; border-radius: 50%; margin-right: 6px; }
  .service-icon.teal { background: var(--teal); }
  .service-icon.orange { background: var(--orange); }
  .service-icon.navy { background: var(--navy); }
  .service-icon.gold { background: var(--gold); }
  .service-name { font-size: 22px; font-weight: 400; color: var(--ink); line-height: 28px; margin-bottom: 0; }
  .service-text { font-size: 17.5px; line-height: 28px; color: var(--body-ink); }
</style>
</head>
<body>
  <nav class="sidebar">
    <div class="menu-toggle"><span></span></div>
    <ul class="nav-list">
      <li><svg viewBox="0 0 16 16"><path d="M8 1 0 8h2v7h4v-5h4v5h4V8h2z"/></svg></li>
      <li><svg viewBox="0 0 16 16"><circle cx="8" cy="4.5" r="3.5"/><path d="M1 15c0-4 3-6 7-6s7 2 7 6z"/></svg></li>
      <li><svg viewBox="0 0 16 16"><circle cx="8" cy="5" r="3"/><circle cx="3" cy="6" r="2"/><circle cx="13" cy="6" r="2"/><path d="M3 14c0-3 2-5 5-5s5 2 5 5zM0 13c0-2 1-4 3-4l1 .3C3 10.5 2.5 12 2.5 13zM16 13c0-2-1-4-3-4l-1 .3c1 1.2 1.5 2.7 1.5 3.7z"/></svg></li>
      <li><svg viewBox="0 0 16 16"><path d="M0 1h3l1 2h12l-2 7H5l-.5 1.5H14V13H3l1.5-3.5L2 2.5H0z"/><circle cx="5" cy="14.5" r="1.5"/><circle cx="12" cy="14.5" r="1.5"/></svg></li>
      <li><svg viewBox="0 0 16 16"><path d="M3 0h7l4 4v12H3zM10 0v4h4z"/></svg></li>
      <li><svg viewBox="0 0 16 16"><path d="M2 3h12v8H2zM0 12h16v2H0z"/></svg></li>
      <li><svg viewBox="0 0 16 16"><path d="M8 1 0 8h2v7h4v-5h4v5h4V8h2z"/></svg></li>
      <li><svg viewBox="0 0 16 16"><circle cx="8" cy="5" r="3"/><circle cx="3" cy="6" r="2"/><circle cx="13" cy="6" r="2"/><path d="M3 14c0-3 2-5 5-5s5 2 5 5z"/></svg></li>
      <li><svg viewBox="0 0 16 16"><path d="M0 3h6l1.5 2H16v9H0z"/></svg></li>
    </ul>
  </nav>

  <div class="hero-band"></div>

  <section class="services">
    <h2 class="section-title">Our Services</h2>
    <p class="section-subtitle">We are Unique Experts</p>

    <div class="service-grid">
      <article class="service-card">
        <div class="service-icon teal" role="img" aria-label="Flat illustration of a desktop monitor"></div>
        <h3 class="service-name">Creativity</h3>
        <p class="service-text">Lorem ipsum dolor sit amet, consectetur adipisicing elit, sed do eiusmod.sunt in culpa qui officia deserunt mollit anim id est laborum.</p>
      </article>
      <article class="service-card">
        <div class="service-icon orange" role="img" aria-label="Flat illustration of a browser window"></div>
        <h3 class="service-name">Design</h3>
        <p class="service-text">Lorem ipsum dolor sit amet, consectetur adipisicing elit, sed do eiusmod.sunt in culpa qui officia deserunt mollit anim id est laborum.</p>
      </article>
      <article class="service-card">
        <div class="service-icon navy" role="img" aria-label="Flat illustration of an open box"></div>
        <h3 class="service-name">Inspiration</h3>
        <p class="service-text">Lorem ipsum dolor sit amet, consectetur adipisicing elit, sed do eiusmod.sunt in culpa qui officia deserunt mollit anim id est laborum.</p>
      </article>
      <article class="service-card">
        <div class="service-icon gold" role="img" aria-label="Flat illustration of a red gem"></div>
        <h3 class="service-name">Awesome</h3>
        <p class="service-text">Lorem ipsum dolor sit amet, consectetur adipisicing elit, sed do eiusmod.sunt in culpa qui officia deserunt mollit anim id est laborum.</p>
      </article>
      <article class="service-card">
        <div class="service-icon gold" role="img" aria-label="Flat illustration of a chart on an easel"></div>
        <h3 class="service-name">Compatibility</h3>
        <p class="service-text">Lorem ipsum dolor sit amet, consectetur adipisicing elit, sed do eiusmod.sunt in culpa qui officia deserunt mollit anim id est laborum.</p>
      </article>
      <article class="service-card">
        <div class="service-icon navy" role="img" aria-label="Flat illustration of a shopping bag"></div>
        <h3 class="service-name">Latest Made</h3>
        <p class="service-text">Lorem ipsum dolor sit amet, consectetur adipisicing elit, sed do eiusmod.sunt in culpa qui officia deserunt mollit anim id est laborum.</p>
      </article>
    </div>
  </section>
</body>
</html>
```